TriVex Business Card Design - double sided -plumbing local plumbing company

We have a Plumbing company where the design was create through Sketch Hive. We would now like a business card designed as well. We want it to be in the colour version of the logo.

Details below for the card.

Phone Number: 0438 615 247
Email: info@trivexplumbing.example.au
Website: https://trivexplumbing.example.au
We really want a sophisticated design that stand out from the other- informative and timeless.

Target Market(s)

local Canberra market

Industry/Entity Type

Plumbing, gas fitting, hot water

Contact Information for Business Card

Phone number, email, logo and "Supplying all your heating, cooling and hot water needs"

Requirements
Must have
• bust be colourful, must also be though about it being printed on a magnet. must Vex with the logo - I dont want the logo and information chucked onto a white canvas I would prefer it to be smooth and look purposeful

```html
<!DOCTYPE html>
<html lang="en">
<head>
<meta charset="utf-8">
<title>TriVex Plumbing – Business Card</title>
<link rel="stylesheet" href="https://fonts.googleapis.com/css2?family=Poppins:ital,wght@0,400;0,600;0,700;1,400&display=swap">
<style>
  :root {
    --stage: #2a2a2a;
    --brand-blue: #0a78bd;
    --line-blue: #2aa3dc;
    --brand-orange: #f8ad3c;
    --paper: #ffffff;
    --card-w: 760px;
    --card-h: 434px;
  }
  * { box-sizing: border-box; margin: 0; padding: 0; }
  html, body {
    width: 1200px; height: 1200px; overflow: hidden;
    background: var(--stage);
    font-family: "Poppins", sans-serif;
  }
  .stage {
    width: 1200px; height: 1200px;
    display: flex; flex-direction: column;
    align-items: center; justify-content: center;
    gap: 60px;
  }
  .card {
    position: relative;
    width: var(--card-w); height: var(--card-h);
    overflow: hidden;
    box-shadow: 10px 12px 0 #1c1c1c;
  }

  /* Contact side */
  .card--contact { background: var(--paper); }
  .brand-lockup {
    position: absolute; left: 70px; top: 0; height: 100%;
    display: flex; align-items: center; gap: 12px;
  }
  .brand-dot {
    width: 22px; height: 22px; border-radius: 50%;
    background: var(--brand-orange);
  }
  .brand-name {
    font-weight: 700; font-size: 44px; line-height: 1;
    color: var(--brand-blue); letter-spacing: 1px;
  }
  .brand-sub {
    display: block; font-weight: 700; font-size: 44px; line-height: 1.05;
    color: var(--brand-blue);
  }
  .divider {
    position: absolute; left: 372px; top: 104px;
    width: 2px; height: 226px; background: var(--line-blue);
  }
  .contact-list {
    position: absolute; left: 414px; top: 150px;
    list-style: none; display: flex; flex-direction: column; gap: 20px;
  }
  .contact-item {
    display: flex; align-items: center; gap: 16px;
    font-size: 15px; color: var(--brand-blue);
  }
  .contact-icon {
    width: 28px; height: 28px; border-radius: 50%;
    background: var(--brand-orange);
    display: flex; align-items: center; justify-content: center;
    flex: none;
  }
  .contact-icon svg { width: 16px; height: 16px; }
  .accent-band {
    position: absolute; bottom: 0; height: 16px;
  }
  .accent-band--blue { left: 410px; width: 190px; background: var(--brand-blue); }
  .accent-band--orange { left: 612px; width: 148px; background: var(--brand-orange); }

  /* Tagline side */
  .card--tagline {
    background: var(--brand-blue);
    display: flex; flex-direction: column;
    align-items: center; justify-content: center;
    gap: 18px;
  }
  .tagline-brand {
    display: flex; align-items: center; gap: 16px;
  }
  .tagline-brand .brand-name {
    color: var(--paper); font-size: 78px; font-weight: 600;
  }
  .tagline-brand .brand-dot { width: 30px; height: 30px; }
  .tagline {
    font-style: italic; font-size: 21px; line-height: 1.3;
    color: var(--paper); text-align: center;
  }
</style>
</head>
<body>
<main class="stage">

  <section class="card card--contact" aria-label="Business card, contact side">
    <div class="brand-lockup">
      <span class="brand-dot" aria-hidden="true"></span>
      <p class="brand-name">TriVex<span class="brand-sub">Plumbing</span></p>
    </div>

    <div class="divider" aria-hidden="true"></div>

    <ul class="contact-list">
      <li class="contact-item">
        <span class="contact-icon" aria-hidden="true">
          <svg viewBox="0 0 24 24"><path fill="#fff" d="M6.6 10.8a15.1 15.1 0 0 0 6.6 6.6l2.2-2.2c.3-.3.7-.4 1-.2 1.1.4 2.3.6 3.6.6.6 0 1 .4 1 1V20c0 .6-.4 1-1 1A17 17 0 0 1 3 4c0-.6.4-1 1-1h3.5c.6 0 1 .4 1 1 0 1.3.2 2.5.6 3.6.1.3 0 .7-.2 1z"/></svg>
        </span>
        0438 615 247
      </li>
      <li class="contact-item">
        <span class="contact-icon" aria-hidden="true">
          <svg viewBox="0 0 24 24"><rect x="3" y="6" width="18" height="12" rx="1.5" fill="none" stroke="#fff" stroke-width="2"/><path d="M3.5 7l8.5 6 8.5-6" fill="none" stroke="#fff" stroke-width="2"/></svg>
        </span>
        info@trivexplumbing.example.au
      </li>
      <li class="contact-item">
        <span class="contact-icon" aria-hidden="true">
          <svg viewBox="0 0 24 24" fill="none" stroke="#fff" stroke-width="1.8"><circle cx="12" cy="12" r="9"/><ellipse cx="12" cy="12" rx="4" ry="9"/><path d="M3 12h18M5 7h14M5 17h14"/></svg>
        </span>
        trivexplumbing.example.au
      </li>
    </ul>

    <div class="accent-band accent-band--blue" aria-hidden="true"></div>
    <div class="accent-band accent-band--orange" aria-hidden="true"></div>
  </section>

  <section class="card card--tagline" aria-label="Business card, brand side">
    <div class="tagline-brand">
      <p class="brand-name">TriVex</p>
      <span class="brand-dot" aria-hidden="true"></span>
    </div>
    <p class="tagline">"Supplying all your heating, cooling<br>and hot water needs"</p>
  </section>

</main>
</body>
</html>
```